signage for belvora rx (pharmacy and surgical supply)

we created logo for belvora rx , we want to see if it could be modified , also we need signage. please review the attachment

```html
<!DOCTYPE html>
<html lang="en">
<head>
<meta charset="utf-8">
<title>Belvora Rx Storefront Sign</title>
<link href="https://fonts.googleapis.com/css2?family=Yellowtail&family=Playfair+Display:wght@400;600&family=Oswald:wght@700&display=swap" rel="stylesheet">
<style>
  :root {
    --page-bg: #ffffff;
    --sign-plum: #3a1c33;
    --sign-rim: #ffffff;
    --brand-ink: #2a9bd6;
    --juice-green: #6a9a3a;
    --spa-rose: #b8557a;
    --pharmacy-red: #e0242b;
  }
  html, body {
    margin: 0;
    width: 1200px;
    height: 854px;
    overflow: hidden;
    background: var(--page-bg);
  }
  .canvas {
    width: 1200px;
    height: 854px;
    display: flex;
    align-items: center;
    justify-content: center;
  }
  .storefront-sign { width: 1000px; height: auto; display: block; }
  .sign-panel { fill: var(--sign-plum); }
  .sign-oval { fill: var(--sign-plum); stroke: var(--sign-rim); stroke-width: 5; }
  .brand-name { font-family: "Oswald", sans-serif; font-weight: 700; fill: var(--brand-ink); }
  .juice-bar { font-family: "Yellowtail", cursive; fill: var(--juice-green); }
  .spa-name { font-family: "Playfair Display", serif; font-weight: 400; fill: var(--spa-rose); }
  .spa-service { font-family: "Playfair Display", serif; font-weight: 600; fill: var(--spa-rose); }
  .pharmacy-title, .pharmacy-sub { font-family: "Oswald", sans-serif; font-weight: 700; fill: var(--pharmacy-red); }
</style>
</head>
<body>
<main class="canvas">
  <svg class="storefront-sign" viewBox="0 0 741 362" role="img" aria-label="Storefront sign for Belvora Rx pharmacy, juice bar and nail spa">
    <rect class="sign-panel" x="0" y="30" width="741" height="303"/>
    <ellipse class="sign-oval" cx="370.5" cy="181" rx="368" ry="178"/>

    <g class="tenant tenant-pharmacy-brand" text-anchor="middle">
      <text class="brand-name" x="207" y="150" font-size="46">BELVORA RX</text>
    </g>

    <g class="tenant tenant-juice">
      <text class="juice-bar" x="388" y="140" font-size="78" textLength="280" lengthAdjust="spacingAndGlyphs">Juice Bar</text>
    </g>

    <g class="tenant tenant-spa" text-anchor="middle">
      <text class="spa-name" x="207" y="236" font-size="38">Rose Petal</text>
      <text class="spa-service" x="207" y="282" font-size="48" textLength="278" lengthAdjust="spacingAndGlyphs">NAILS &amp; SPA</text>
    </g>

    <g class="tenant tenant-pharmacy">
      <text class="pharmacy-title" x="388" y="255" font-size="58" textLength="276" lengthAdjust="spacingAndGlyphs">PHARMACY</text>
      <text class="pharmacy-sub" x="388" y="282" font-size="27" textLength="278" lengthAdjust="spacingAndGlyphs">&amp; SURGICAL SUPPLY</text>
    </g>
  </svg>
</main>
</body>
</html>
```